WordPress Blog/Website for Athlete Focused Sports Marketing Agency

WordPress Website that Serves two primary purposes:

1) Company Information Website which showcases organization's capabilities and work

2) Highlights, Showcases and Displays key information for athlete clients, aggregates all of the content they are creating(mostly social) and is a key portal for publishing press releases, news updates and more.

Key Criteria for Success:

Easily Updatable
Easy to Navigate
Clean Design that follows the function/form of the organization's brand identity while also incorporating the identity of the athletes.

Supporting Documentation:**These files are also uploaded and attached to this project description**
Creative Brief: https://files.briskhollow.net/a/lanternmoor.com/file/d/7KxR2mTqWvB9pLnYcHsDfJgZaQe/edit?usp=sharing
Logo Files/Designs are attached. Color Palette can be adjusted as necessary.

WireFrame: (Please use your own judgement and creative liberty's to make something that is a lot better then what I came up with):
https://files.briskhollow.net/file/d/7KxR2mTqWvB9pXtNbVcMwQrLsKy/edit?usp=sharing

Current Website(Incomplete): www.lanternmoor.com

Thanks!

Industry/Entity Type

It Company

Requirements
Must have
• Social Media Integration: A social feed that aggregates content across all channels for multiple users(all of my athletes)

"News=Blog" Portal that serves as the primary engine for the page's content

Professional Look and Design- it should look like a website, not a blog.

```html
<!DOCTYPE html>
<html lang="en">
<head>
<meta charset="utf-8">
<title>Lantern &amp; Moor — Athlete Sports Marketing</title>
<link href="https://fonts.googleapis.com/css2?family=Open+Sans:wght@400;600;700&family=Roboto+Condensed:wght@400;700&family=Rokkitt:wght@400;600&family=Trocchi&family=Raleway:wght@300;400&display=swap" rel="stylesheet">
<style>
:root{
  --orange:#f07a1a;
  --ink:#222;
  --text:#555;
  --line:#ddd;
  --footer:#2c2c2c;
  --footer-text:#9a9a9a;
  --white:#fff;
}
*{box-sizing:border-box;margin:0;padding:0}
html,body{width:1200px;height:2662px;overflow:hidden}
body{position:relative;background:var(--white);font-family:"Open Sans",Arial,sans-serif;color:var(--text)}
.abs{position:absolute}

/* header */
.top-rule{left:0;top:0;width:1200px;height:6px;background:#333}
.logo{left:140px;top:26px;display:flex;align-items:center}
.logo-name{font-family:"Rokkitt",Georgia,serif;font-size:54px;font-weight:400;color:var(--orange);letter-spacing:.5px;line-height:60px}
.contact{right:140px;top:28px;text-align:right}
.contact .call{font-size:22px;color:var(--ink)}
.contact .mail{font-size:15px;color:var(--orange);margin-top:2px}

.nav{left:140px;top:106px;width:918px;height:52px;background:var(--orange);display:flex;align-items:center}
.nav a{font-family:"Roboto Condensed",Arial,sans-serif;font-weight:700;font-size:15px;color:#fff;text-decoration:none;text-transform:uppercase;padding:0 22px;height:52px;line-height:52px}
.nav a.active{background:#333}
.nav .social{margin-left:auto;display:flex;gap:8px;padding-right:14px}
.nav .social span{width:30px;height:30px;border-radius:50%;background:#fff}

/* slider */
.slider-band{left:0;top:166px;width:1200px;height:477px;background:repeating-linear-gradient(45deg,#3a3a3a 0 3px,#404040 3px 6px)}
.slide{left:149px;top:170px;width:900px;height:456px;background:linear-gradient(180deg,#cfd9e2 0%,#a9b7c4 40%,#7d7f80 70%,#5f8a3a 100%);box-shadow:0 4px 14px rgba(0,0,0,.5)}
.slide-caption{left:149px;top:470px;width:782px;height:107px;background:rgba(20,20,20,.72);padding:14px 20px}
.slide-caption h2{font-family:"Roboto Condensed",sans-serif;font-weight:400;font-size:34px;color:#fff;line-height:38px}
.slide-caption p{font-size:14px;color:#eee;margin-top:8px;line-height:20px;font-weight:600}
.arrow{top:380px}
.dots{left:560px;top:608px;display:flex;gap:8px;background:rgba(255,255,255,.85);padding:4px 8px;border-radius:10px}
.dots i{width:8px;height:8px;border-radius:50%;background:#555;display:block}
.dots i.on{background:var(--orange)}

/* welcome */
.ribbon{left:320px;top:674px;width:560px;height:50px}
.ribbon-text{left:320px;top:674px;width:560px;height:50px;text-align:center;line-height:50px;font-family:"Trocchi",Georgia,serif;font-size:25px;color:#fff;letter-spacing:1.5px}
.intro{left:140px;top:738px;width:918px;text-align:center;font-size:14.5px;line-height:23px;color:#555}

/* section titles */
.section-title{font-family:"Roboto Condensed",sans-serif;font-weight:700;font-size:22px;color:#333;text-transform:uppercase}
.section-rule{height:4px;background:var(--orange)}
.section-rule::after{content:"";position:absolute;left:22px;top:4px;border:7px solid transparent;border-top-color:var(--orange)}

/* services */
.services{left:140px;top:940px;width:918px;display:flex}
.service{flex:1;text-align:center;padding:0 14px}
.service svg{height:56px}
.service .kicker{font-size:14px;color:#333;margin-top:8px;white-space:nowrap}
.service .name{font-family:"Roboto Condensed",sans-serif;font-weight:700;font-size:16px;color:var(--orange);text-transform:uppercase;letter-spacing:.5px;white-space:nowrap}
.service p{font-size:12.5px;line-height:19px;color:#666;margin-top:12px;height:76px;padding:0 10px}
.btn{display:inline-block;font-size:10px;color:#444;background:linear-gradient(#f4f4f4,#dcdcdc);border:1px solid #ccc;border-radius:3px;padding:4px 14px;margin-top:14px}

/* blogs */
.blog-list{left:140px;top:1304px;width:432px}
.post{display:flex;gap:16px;height:106px}
.thumb{width:90px;height:90px;flex:none;border:5px solid #eee;box-shadow:0 0 0 1px #ddd;background:linear-gradient(160deg,#8aa0b4,#a87a5a)}
.post h3{font-size:12.5px;font-weight:700;color:#222;margin-top:2px}
.post p{font-size:12.5px;line-height:18px;color:#555;margin-top:4px}
.post .btn{margin-top:6px;padding:3px 10px}

.video{left:605px;top:1304px;width:453px;height:337px;background:#1e1e1e;box-shadow:0 0 0 1px #444}
.video .play{left:190px;top:127px}
.video-bar{left:0;bottom:0;width:453px;height:40px;background:#2a2a2a}
.video-progress{left:6px;bottom:30px;width:441px;height:4px;background:#555}
.video-progress::before{content:"";position:absolute;left:0;top:-3px;width:10px;height:10px;border-radius:50%;background:#e33}
.video-time{left:70px;bottom:8px;font-size:11px;color:#ccc}

/* gallery */
.gallery{left:140px;top:1757px;width:918px;display:flex;gap:12px}
.gallery .tile{flex:1;height:178px;border:6px solid #e8e8e8;box-shadow:0 0 0 1px #ccc}

/* clients */
.clients-a{left:150px;top:2058px;width:898px;display:flex;gap:20px}
.clients-b{left:150px;top:2207px;width:898px;display:flex;gap:16px}
.client{flex:1;border:1px solid #ccc;box-shadow:inset 0 0 0 5px #f4f4f4;display:flex;align-items:center;justify-content:center;gap:10px;font-weight:700;color:#333;white-space:nowrap}
.clients-a .client{height:116px;font-size:26px}
.clients-b .client{height:89px;font-size:19px}
.client .dot{width:18px;height:18px;border-radius:50%;background:#333}

/* footer */
.footer{left:0;top:2347px;width:1200px;height:315px;background:var(--footer)}
.quick-title{left:140px;top:2380px;font-family:"Roboto Condensed",sans-serif;font-weight:700;font-size:22px;color:var(--orange);text-transform:uppercase}
.quick-links{left:140px;top:2425px;display:flex;gap:64px}
.quick-links ul{list-style:none}
.quick-links li{font-size:12.5px;color:var(--footer-text);line-height:28px}
.quick-links li::before{content:"›";color:#666;margin-right:8px}
.footer-phone{left:710px;top:2375px;font-family:"Raleway",sans-serif;font-weight:300;font-size:42px;color:#fff;line-height:50px}
.footer-mail{left:712px;top:2427px;font-size:13px;color:#777}
.footer-social{left:712px;top:2454px;display:flex;gap:6px}
.footer-social span{width:18px;height:18px;border-radius:50%;background:#666}
.share{left:712px;top:2484px;display:flex;gap:6px}
.share span{width:48px;height:20px;background:#e8e8e8;border-radius:3px}
.copyright{left:712px;top:2537px;font-size:11px;color:#777}
.footer-rule{left:140px;top:2577px;width:918px;height:1px;background:#444}
.enquiry{left:162px;top:2604px;font-size:15px;color:#bbb;text-transform:uppercase;letter-spacing:.3px}
.enquiry a{color:var(--orange);text-decoration:none}
.subscribe{left:872px;top:2598px;width:164px;height:32px;background:var(--orange);color:#fff;font-size:13px;font-weight:600;text-transform:uppercase;display:flex;align-items:center;justify-content:center;gap:8px}
</style>
</head>
<body>

<header>
  <div class="abs top-rule"></div>
  <div class="abs logo">
    <div class="logo-name">Lantern &amp; Moor</div>
  </div>
  <div class="abs contact">
    <div class="call">Call: 555-013-2468</div>
    <div class="mail">Email: hello@lanternmoor.com</div>
  </div>
  <nav class="abs nav">
    <a class="active">Home</a>
    <a>What We Do?</a>
    <a>Athletes</a>
    <a>Gallery</a>
    <a>Contact</a>
    <div class="social"><span></span><span></span><span></span></div>
  </nav>
</header>

<section>
  <div class="abs slider-band"></div>
  <div class="abs slide" role="img" aria-label="Cyclist in helmet riding hard under a cloudy sky, green grass below"></div>
  <svg class="abs arrow" style="left:178px" width="24" height="48" viewBox="0 0 24 48"><polyline points="20,4 4,24 20,44" fill="none" stroke="#fff" stroke-width="3" opacity=".8"/></svg>
  <svg class="abs arrow" style="left:996px" width="24" height="48" viewBox="0 0 24 48"><polyline points="4,4 20,24 4,44" fill="none" stroke="#fff" stroke-width="3" opacity=".8"/></svg>
  <div class="abs slide-caption">
    <h2>Athlete Brand Building</h2>
    <p>Think 'athlete representatives who spent their careers managing some of the world's biggest brands and sponsoring athletes themselves'.</p>
  </div>
  <div class="abs dots"><i class="on"></i><i></i><i></i><i></i></div>
</section>

<section>
  <svg class="abs ribbon" viewBox="0 0 560 50" preserveAspectRatio="none">
    <polygon points="0,0 560,0 546,25 560,50 0,50 14,25" fill="#3a3a3a"/>
    <circle cx="36" cy="25" r="4" fill="#fff"/><circle cx="524" cy="25" r="4" fill="#fff"/>
  </svg>
  <div class="abs ribbon-text">WELCOME TO LANTERN &amp; MOOR</div>
  <p class="abs intro">Lorem Ipsum is simply dummy text of the printing and typesetting industry. Lorem Ipsum has been the industry's standard dummy text ever since the 1500s, when an unknown printer took a galley of type and scrambled it to make a type specimen book. It has survived not only five centuries, but also the leap into electronic typesetting, remaining essentially unchanged.</p>
</section>

<section>
  <h2 class="abs section-title" style="left:140px;top:868px">Our Services</h2>
  <div class="abs section-rule" style="left:140px;top:903px;width:918px"></div>
  <div class="abs services">
    <div class="service">
      <svg viewBox="0 0 40 56" width="40"><circle cx="20" cy="18" r="13" fill="none" stroke="#222" stroke-width="5"/><rect x="14" y="34" width="12" height="5" fill="#222"/><rect x="14" y="42" width="12" height="5" fill="#222"/></svg>
      <div class="kicker">Athlete</div>
      <div class="name">Brand Building</div>
      <p>Think 'athlete representatives who spent their careers managing some of the world's biggest brands...</p>
      <span class="btn">Read More...</span>
    </div>
    <div class="service">
      <svg viewBox="0 0 76 56" width="76"><g fill="none" stroke="#222" stroke-width="4"><circle cx="16" cy="38" r="12"/><circle cx="60" cy="38" r="12"/><polyline points="16,38 30,18 50,18 60,38"/><polyline points="30,18 38,38 50,18"/><line x1="26" y1="12" x2="34" y2="12"/><line x1="50" y1="18" x2="48" y2="10"/></g></svg>
      <div class="kicker">Lifestyle &amp;</div>
      <div class="name">Sports Marketing</div>
      <p>Be relevant, be passionate and connect with consumers in a credible way in a natural environment while building...</p>
      <span class="btn">Read More...</span>
    </div>
    <div class="service">
      <svg viewBox="0 0 56 56" width="56"><circle cx="24" cy="24" r="18" fill="#222"/><polygon points="36,34 52,50 46,54 32,38" fill="#222"/></svg>
      <div class="kicker">Marketing &amp; Communications</div>
      <div class="name">Planning &amp; Design</div>
      <p>Print, Digital, Social and Experiential Marketing are all part of a bigger picture which defines your brand.</p>
      <span class="btn">Read More...</span>
    </div>
    <div class="service">
      <svg viewBox="0 0 56 56" width="56"><path d="M8 22h12a6 6 0 1 1 12 0h10v12a6 6 0 1 1 0 12v6H8v-10a6 6 0 1 0 0-12z" fill="#222"/></svg>
      <div class="kicker">Product Strategy</div>
      <div class="name">&amp; Launches</div>
      <p>Product Launches and Product Strategy can redefine the success of your organization. We have launched...</p>
      <span class="btn">Read More...</span>
    </div>
  </div>
</section>

<section>
  <h2 class="abs section-title" style="left:140px;top:1232px">Our Blogs</h2>
  <div class="abs section-rule" style="left:140px;top:1267px;width:432px"></div>
  <div class="abs blog-list">
    <article class="post"><div class="thumb" role="img" aria-label="Athlete portrait thumbnail"></div><div><h3>Lorem Ipsum is simply dummy text</h3><p>Lorem ipsum dolor sit amet, consectetuer adipiscing elit. Nam cursus. Morbi ut mi.</p><span class="btn">Read More...</span></div></article>
    <article class="post"><div class="thumb" role="img" aria-label="Athlete portrait thumbnail"></div><div><h3>Lorem Ipsum is simply dummy text</h3><p>Lorem ipsum dolor sit amet, consectetuer adipiscing elit. Nam cursus. Morbi ut mi.</p><span class="btn">Read More...</span></div></article>
    <article class="post"><div class="thumb" role="img" aria-label="Athlete portrait thumbnail"></div><div><h3>Lorem Ipsum is simply dummy text</h3><p>Lorem ipsum dolor sit amet, consectetuer adipiscing elit. Nam cursus. Morbi ut mi.</p><span class="btn">Read More...</span></div></article>
  </div>

  <h2 class="abs section-title" style="left:605px;top:1232px">Our Video</h2>
  <div class="abs section-rule" style="left:605px;top:1267px;width:453px"></div>
  <div class="abs video">
    <svg class="abs play" width="72" height="72" viewBox="0 0 72 72"><circle cx="36" cy="36" r="32" fill="none" stroke="#555" stroke-width="4"/><polygon points="29,22 52,36 29,50" fill="#555"/></svg>
    <div class="abs video-bar"></div>
    <div class="abs video-progress"></div>
    <svg class="abs" style="left:14px;bottom:10px" width="40" height="16" viewBox="0 0 40 16"><rect x="2" y="2" width="4" height="12" fill="#ccc"/><rect x="10" y="2" width="4" height="12" fill="#ccc"/><polygon points="22,3 34,8 22,13" fill="#ccc"/></svg>
    <div class="abs video-time">0:01 / 3:35</div>
  </div>
</section>

<section>
  <h2 class="abs section-title" style="left:140px;top:1682px">Our Gallery</h2>
  <div class="abs section-rule" style="left:140px;top:1717px;width:918px"></div>
  <div class="abs gallery">
    <div class="tile" role="img" aria-label="Hurdler clearing a hurdle on the track" style="background:linear-gradient(160deg,#2f3e78,#b85a3a)"></div>
    <div class="tile" role="img" aria-label="Athlete celebrating at a race finish" style="background:linear-gradient(160deg,#e3e6ea,#c49b7f)"></div>
    <div class="tile" role="img" aria-label="Lacrosse players on a green field" style="background:linear-gradient(160deg,#3d3d50,#4f8f3c)"></div>
    <div class="tile" role="img" aria-label="Rider on horseback clearing a jump" style="background:linear-gradient(160deg,#8fb4da,#8a5530)"></div>
  </div>
</section>

<section>
  <h2 class="abs section-title" style="left:140px;top:1985px">Key Client</h2>
  <div class="abs section-rule" style="left:140px;top:2016px;width:918px"></div>
  <div class="abs clients-a">
    <div class="client">Stridek</div>
    <div class="client" style="font-size:17px">Camber Creative Works</div>
    <div class="client">Veltran</div>
    <div class="client">Everstride</div>
  </div>
  <div class="abs clients-b">
    <div class="client"><span class="dot"></span>Bavelo</div>
    <div class="client">Tellox</div>
    <div class="client">Kotaro</div>
    <div class="client"><span class="dot"></span>Orbis</div>
    <div class="client">Apsley</div>
  </div>
</section>

<footer>
  <div class="abs footer"></div>
  <h2 class="abs quick-title">Quick Links</h2>
  <div class="abs quick-links">
    <ul><li>Home</li><li>What We Do?</li><li>Athletes</li><li>Gallery</li><li>Contact</li></ul>
    <ul><li>Privacy Policy</li><li>Career</li><li>Sitemap</li></ul>
  </div>
  <div class="abs footer-phone">0555.013.2468</div>
  <div class="abs footer-mail">info@lanternmoor.com</div>
  <div class="abs footer-social"><span></span><span></span><span></span></div>
  <div class="abs share"><span></span><span></span><span></span></div>
  <div class="abs copyright">Copyright © 2013 Lanternmoor. All Rights Reserved.</div>
  <div class="abs footer-rule"></div>
  <div class="abs enquiry">Have a question or just wish to make a general enquiry? <a>Get in touch.</a></div>
  <div class="abs subscribe">Subscribe Now!
    <svg width="18" height="12" viewBox="0 0 18 12"><rect x="1" y="1" width="16" height="10" fill="none" stroke="#fff" stroke-width="1.5"/><polyline points="1,1 9,7 17,1" fill="none" stroke="#fff" stroke-width="1.5"/></svg>
  </div>
</footer>

</body>
</html>
```